Keystone Lending and Capital. We provide MOSTLY residential home mortgages in Florida AND commercial loans for investment properties throughout the United states.
I would love to emulate so of the lender sites that are available on the internet but I would like to have the site as popular as possible for SEO purposes. Clients can already click the link to take them to the mortgage application where they can complete that and upload documents. If you could polish that up for me that would be great. I can also provide you with great detail on loan programs that are currently being offered. WE OFFER ALL MORTGAGE LENDING PRODUCTS. I would also like to add something in reference to the rate but I don't think it's legal to actually state or promise a rate for mortgage since they vary based on loan type, client and other criteria...

On the Keystone real estate site I would like to add a link or some way for clients to be able to put in credit card information to render services ...

Please let me know what you need from me

Thank you !!

Current link to site to improve and code

https://keystonelendingandcapital.example/

Residential and commmercial lending

Requirements
Must have
• Love to integrate Mortgage interest rates even if general
Nice to have
• Link to fill out mortgage application via Vanta LOS software

```html
<!DOCTYPE html>
<html lang="en">
<head>
<meta charset="utf-8">
<title>Keystone Lending and Capital</title>
<link href="https://fonts.googleapis.com/css2?family=Montserrat:wght@400;500;600;700;800&display=swap" rel="stylesheet">
<style>
  :root {
    --green: #8db83f;
    --green-dark: #1f3d1d;
    --green-soft: #eef4e3;
    --ink: #1b2a17;
    --white: #ffffff;
    --muted: #6b6b6b;
    --line: #d9d9d9;
  }
  * { box-sizing: border-box; margin: 0; padding: 0; }
  html, body { width: 796px; height: 1200px; overflow: hidden; }
  body { font-family: 'Montserrat', sans-serif; color: var(--ink); background: var(--white); }

  .site-header { height: 53px; display: flex; align-items: center; justify-content: space-between; padding: 0 40px 0 72px; }
  .brand { display: flex; align-items: center; gap: 8px; }
  .brand-mark { width: 18px; height: 18px; background: var(--green-dark); }
  .brand-name { font-size: 7.5px; font-weight: 700; color: var(--green-dark); line-height: 1.35; letter-spacing: .3px; }
  .main-nav { display: flex; gap: 22px; font-size: 7.5px; font-weight: 500; }
  .main-nav a { color: var(--ink); text-decoration: none; }

  .hero { position: relative; height: 372px; overflow: hidden; }
  .hero-photo { position: absolute; inset: 0;
    background: linear-gradient(180deg, #c7a37a 0%, #e4b885 18%, #8c8a74 40%, #5d7a4a 65%, #3f5e33 100%); }
  .hero-shape { position: absolute; inset: 0; }
  .hero-content { position: relative; padding: 68px 0 0 40px; width: 320px; }
  .hero-kicker { font-size: 10.5px; font-weight: 700; color: var(--green-dark); line-height: 1.35; margin-bottom: 10px; }
  .hero-title { font-size: 17px; font-weight: 800; color: var(--green-dark); line-height: 1.25; margin-bottom: 22px; }
  .btn-apply { display: inline-block; background: var(--green-dark); color: var(--white); font-size: 6.5px; font-weight: 700;
    padding: 8px 12px; text-decoration: none; letter-spacing: .2px; }

  .rates { height: 74px; background: var(--green-soft); display: flex; align-items: center; padding: 0 72px; gap: 18px; }
  .rates-head { width: 150px; }
  .rates-title { font-size: 11px; font-weight: 800; color: var(--green-dark); line-height: 1.2; }
  .rates-note { font-size: 5px; color: var(--muted); margin-top: 4px; line-height: 1.4; }
  .rate-list { flex: 1; display: flex; gap: 10px; }
  .rate-item { flex: 1; background: var(--white); border-left: 3px solid var(--green); padding: 7px 8px; }
  .rate-label { font-size: 5.5px; font-weight: 600; color: var(--muted); text-transform: uppercase; letter-spacing: .3px; }
  .rate-value { font-size: 12px; font-weight: 800; color: var(--green-dark); margin-top: 3px; }
  .rate-value small { font-size: 5.5px; font-weight: 600; color: var(--muted); }

  .properties { height: 296px; padding-top: 26px; }
  .section-title { display: flex; align-items: center; justify-content: center; gap: 8px; font-size: 22px; font-weight: 800; }
  .section-title .t-dark { color: var(--green-dark); }
  .section-title .t-green { color: var(--green); }
  .title-dot { width: 18px; height: 18px; border-radius: 50%; background: var(--green-dark); }
  .property-list { display: flex; gap: 14px; justify-content: center; margin-top: 22px; }
  .property-card { position: relative; width: 150px; height: 190px; border-radius: 4px; overflow: hidden; }
  .property-card .photo { position: absolute; inset: 0; }
  .photo-1 { background: linear-gradient(180deg, #4a7fc0 0%, #8fb1d6 45%, #2b3b52 100%); }
  .photo-2 { background: linear-gradient(180deg, #1b2b4a 0%, #35507a 50%, #1a2233 100%); }
  .photo-3 { background: linear-gradient(180deg, #a9c3e0 0%, #d6d4cc 50%, #3a3a36 100%); }
  .photo-4 { background: linear-gradient(180deg, #7fa3c9 0%, #4e6a8d 50%, #23324a 100%); }
  .property-card::after { content: ""; position: absolute; inset: 0; background: linear-gradient(180deg, transparent 55%, rgba(0,0,0,.65)); }
  .tag { position: absolute; top: 8px; left: 8px; z-index: 1; background: var(--white); font-size: 4.5px; font-weight: 700; padding: 2px 5px; border-radius: 2px; }
  .card-info { position: absolute; left: 9px; bottom: 12px; z-index: 1; color: var(--white); }
  .card-name { font-size: 8.5px; font-weight: 700; }
  .card-place { font-size: 4.5px; margin-top: 3px; }
  .pager { display: flex; justify-content: center; gap: 4px; margin-top: 16px; }
  .pager span { width: 5px; height: 2px; background: var(--line); }
  .pager span.active { width: 14px; background: var(--muted); }

  .contact { position: relative; height: 360px; background: linear-gradient(180deg, #2a4d26, #1e3a1c); color: var(--white); padding-top: 34px; }
  .contact-photo { position: absolute; inset: 0; background: radial-gradient(ellipse at 70% 70%, rgba(120,150,100,.25), transparent 60%); }
  .contact .section-title { position: relative; color: var(--white); }
  .contact .title-dot { background: var(--green); }
  .contact-lead { position: relative; text-align: center; font-size: 6px; margin-top: 10px; }
  .contact-form { position: relative; width: 260px; margin: 14px auto 0; }
  .field { margin-bottom: 8px; }
  .field label { display: block; font-size: 5.5px; font-weight: 600; margin-bottom: 3px; }
  .field .input { height: 17px; background: var(--white); border-radius: 2px; }
  .field .textarea { height: 46px; background: var(--white); border-radius: 2px; }
  .btn-send { display: block; width: 100%; height: 18px; background: var(--green); color: var(--white); border: 0; font: 600 7px 'Montserrat', sans-serif; border-radius: 2px; }

  .site-footer { height: 45px; display: flex; align-items: center; justify-content: center; font-size: 6px; color: var(--ink); }
</style>
</head>
<body>
  <header class="site-header">
    <div class="brand">
      <span class="brand-mark"></span>
      <div class="brand-name">KEYSTONE LENDING AND CAPITAL OF FLORIDA<br>BUSINESS AND COMMERCIAL DIVISION</div>
    </div>
    <nav class="main-nav"><a href="#">Home</a><a href="#">About</a><a href="#">Properties</a></nav>
  </header>

  <section class="hero">
    <div class="hero-photo" role="img" aria-label="Aerial view of a Florida neighbourhood with trees and buildings at sunset"></div>
    <svg class="hero-shape" viewBox="0 0 796 372" preserveAspectRatio="none">
      <path d="M0 0 H430 C400 120 380 250 330 372 H0 Z" fill="var(--green)"/>
      <path d="M458 0 H488 C458 140 432 260 392 372 H362 C410 250 440 130 458 0 Z" fill="var(--green)"/>
      <path d="M515 0 H540 C512 130 482 270 442 372 H418 C462 260 492 130 515 0 Z" fill="var(--green)"/>
    </svg>
    <div class="hero-content">
      <p class="hero-kicker">RESIDENTIAL HOME LOANS IN<br>FLORIDA AND COMMERCIAL<br>LENDING IN AMERICA</p>
      <h1 class="hero-title">YOUR BEST RESOURCE<br>FOR HASSLE-FREE, LOW<br>COST MORTGAGE<br>ORIGINATION</h1>
      <a class="btn-apply" href="#">FILL OUT MORTGAGE APPLICATION TO BEGIN LENDING TODAY</a>
    </div>
  </section>

  <section class="rates" aria-label="General mortgage rate guide">
    <div class="rates-head">
      <h2 class="rates-title">Today's General<br>Mortgage Rates</h2>
      <p class="rates-note">Rates shown are general market ranges, not an offer. Your rate depends on loan type, credit and other criteria.</p>
    </div>
    <div class="rate-list">
      <div class="rate-item"><div class="rate-label">30-Year Fixed</div><div class="rate-value">6.5–7.1% <small>APR range</small></div></div>
      <div class="rate-item"><div class="rate-label">15-Year Fixed</div><div class="rate-value">5.8–6.4% <small>APR range</small></div></div>
      <div class="rate-item"><div class="rate-label">FHA / VA</div><div class="rate-value">6.1–6.7% <small>APR range</small></div></div>
      <div class="rate-item"><div class="rate-label">Commercial</div><div class="rate-value">7.0–8.5% <small>APR range</small></div></div>
    </div>
  </section>

  <section class="properties">
    <h2 class="section-title"><span class="t-dark">Available</span><span class="title-dot"></span><span class="t-green">Properties</span></h2>
    <div class="property-list">
      <article class="property-card"><div class="photo photo-1" role="img" aria-label="High-rise residential tower"></div><span class="tag">RESIDENTIAL</span><div class="card-info"><div class="card-name">Cedar Grove Trails</div><div class="card-place">● Tampa, Florida</div></div></article>
      <article class="property-card"><div class="photo photo-2" role="img" aria-label="City skyline at night"></div><span class="tag">RESIDENTIAL</span><div class="card-info"><div class="card-name">Cedar Grove Trails</div><div class="card-place">● Tampa, Florida</div></div></article>
      <article class="property-card"><div class="photo photo-3" role="img" aria-label="Modern white house"></div><span class="tag">RESIDENTIAL</span><div class="card-info"><div class="card-name">Cedar Grove Trails</div><div class="card-place">● Tampa, Florida</div></div></article>
      <article class="property-card"><div class="photo photo-4" role="img" aria-label="Apartment block under blue sky"></div><span class="tag">RESIDENTIAL</span><div class="card-info"><div class="card-name">Cedar Grove Trails</div><div class="card-place">● Tampa, Florida</div></div></article>
    </div>
    <div class="pager"><span></span><span></span><span class="active"></span><span></span></div>
  </section>

  <section class="contact">
    <div class="contact-photo" role="img" aria-label="Faint house exterior behind a green tint"></div>
    <h2 class="section-title"><span>Get in</span><span class="title-dot"></span><span>Touch</span></h2>
    <p class="contact-lead">Please send me a message for general inquiries or reservations.</p>
    <form class="contact-form">
      <div class="field"><label>Full Name *</label><div class="input"></div></div>
      <div class="field"><label>Email Address *</label><div class="input"></div></div>
      <div class="field"><label>Phone Number *</label><div class="input"></div></div>
      <div class="field"><label>Message *</label><div class="textarea"></div></div>
      <button class="btn-send" type="button">Send Message</button>
    </form>
  </section>

  <footer class="site-footer">© 2024. All Rights Reserved.</footer>
</body>
</html>
```